FC Morlan - Creation of a AD banner for our yearly event

We are a local soccer club in Switzerland. We're organizing a event that will substitute to our yearly club dinner. We need a banner AD to promote on the social networks this event.
We would like to see design that use one or the 2 colors of the club (blue and red).
This Ad should link to a online shop where we can buy vouchers.

Requirements
Must have
• Logo of the club
Title : Fête des lanternes d'hiver
Call to action : Plus d'informations
Side texte : Grande Tombola
Banner size : W300xH250 or W300xH600
Nice to have
• Promotion texte: Soutenez le FC Morlan et les restaurateurs locaux

```html
<!DOCTYPE html>
<html lang="fr">
<head>
<meta charset="utf-8">
<title>FC Morlan – Fête des lanternes d'hiver</title>
<link rel="stylesheet" href="https://fonts.googleapis.com/css2?family=Abril+Fatface&family=Archivo+Black&family=Arimo:wght@400;700&display=swap">
<style>
  :root {
    --page: #e8e8e8;
    --night: #17161a;
    --club-red: #e8263c;
    --club-blue: #0a86c9;
    --white: #ffffff;
    --ink: #1a1a1a;
    --photo-dark: #0d0d0f;
    --photo-shirt: #d92a3a;
    --photo-grass: #2f7a2a;
  }
  * { box-sizing: border-box; margin: 0; padding: 0; }
  html, body { width: 1200px; height: 1000px; overflow: hidden; background: var(--page); }
  .ad-banner {
    position: absolute; left: 214px; top: 178px;
    width: 772px; height: 644px; overflow: hidden; background: var(--white);
  }
  .ad-shapes { position: absolute; inset: 0; }
  .event-title {
    position: absolute; left: 0; top: 14px; width: 484px;
    font-family: "Abril Fatface", serif; font-weight: 400;
    color: var(--white); font-size: 50px; line-height: 68px;
    text-align: center; letter-spacing: 1px;
  }
  .support-box {
    position: absolute; left: 29px; top: 182px; width: 468px; height: 98px;
    border: 2px solid var(--white);
    display: flex; align-items: center; justify-content: center; text-align: center;
    font-family: "Arimo", sans-serif; color: var(--white);
    font-size: 30px; line-height: 38px;
  }
  .raffle {
    position: absolute; left: 0; width: 466px; text-align: center;
    font-family: "Archivo Black", sans-serif; color: var(--club-red);
    font-size: 70px; line-height: 70px; letter-spacing: 1px;
    -webkit-text-stroke: 3px var(--white); paint-order: stroke fill;
  }
  .raffle-first { top: 338px; }
  .raffle-second { top: 422px; }
  .pointer { position: absolute; left: 210px; top: 507px; }
  .cta-button {
    position: absolute; left: 49px; top: 545px; width: 324px; height: 64px;
    background: var(--club-red); border: 2px solid var(--white);
    display: flex; align-items: center; justify-content: center;
    font-family: "Arimo", sans-serif; color: var(--white); font-size: 26px;
    text-decoration: none;
  }
  .club-mark {
    position: absolute; left: 552px; top: 500px; width: 200px;
    display: flex; flex-direction: column; align-items: center; gap: 14px;
  }
  .club-mark-dot { width: 64px; height: 64px; border-radius: 50%; background: var(--club-red); }
  .club-mark-name {
    font-family: "Arimo", sans-serif; font-weight: 700; color: var(--ink);
    font-size: 30px; line-height: 1;
  }
</style>
</head>
<body>
  <div class="ad-banner">
    <svg class="ad-shapes" width="772" height="644" viewBox="0 0 772 644">
      <defs>
        <linearGradient id="photoTone" x1="0" y1="0" x2="0" y2="1">
          <stop offset="0" stop-color="var(--photo-shirt)"/>
          <stop offset="0.35" stop-color="var(--photo-dark)"/>
          <stop offset="0.8" stop-color="var(--photo-dark)"/>
          <stop offset="1" stop-color="var(--photo-grass)"/>
        </linearGradient>
      </defs>
      <path role="img" aria-label="Photo d'un joueur de football en maillot rouge avec un ballon sur la pelouse"
            d="M470 0 H772 V442 Q660 402 552 372 Z" fill="url(#photoTone)"/>
      <path d="M552 372 Q660 402 772 442 V464 Q660 424 548 388 Z" fill="var(--club-blue)"/>
      <path d="M470 0 H494 C590 150 600 400 392 644 H330 Z" fill="var(--club-red)"/>
      <path d="M0 0 H476 C562 150 560 420 342 644 H0 Z" fill="var(--night)"/>
    </svg>

    <h1 class="event-title">Fête des lanternes<br>d'hiver</h1>

    <p class="support-box">Soutenez le FC Morlan<br>et les restaurateurs locaux</p>

    <p class="raffle raffle-first">GRANDE</p>
    <p class="raffle raffle-second">TOMBOLA</p>

    <svg class="pointer" width="30" height="26" viewBox="0 0 30 26">
      <path d="M0 0 H30 L15 26 Z" fill="var(--club-red)"/>
    </svg>

    <a class="cta-button" href="#">Plus d'informations</a>

    <div class="club-mark">
      <span class="club-mark-dot"></span>
      <span class="club-mark-name">FC Morlan</span>
    </div>
  </div>
</body>
</html>
```